Remodel Flyer for realtors

"T" Ridgeline Builders

4"x 9" rack card front and back

www.BrambleworkHomes.example

555-318-4726

Let us fix what your home inspector finds!

Send us your inspection summary.

We are a licensed and Insured contractor.
CRC8071943

Serving
Marion County and Pelham Hollow

This flyer will sit in realtor offices for realtors to give to there buyers and sellers.

Target Market(s)

Realtors

Industry/Entity Type

Construction

Colors

Designer to choose colors to be used in the design.

```html
<!DOCTYPE html>
<html lang="en">
<head>
<meta charset="utf-8">
<title>"T" Ridgeline Builders – Rack Card Front and Back</title>
<link href="https://fonts.googleapis.com/css2?family=Oswald:wght@300;500;600&family=Open+Sans:wght@400;600&display=swap" rel="stylesheet">
<style>
  :root {
    --orange: #f29a1f;
    --orange-deep: #e8880f;
    --charcoal: #55585b;
    --ink: #3b3b3b;
    --paper: #ffffff;
    --backdrop: #c4c4c4;
    --footer-light: #8a8a8a;
    --footer-dark: #5e5e5e;
  }
  * { box-sizing: border-box; margin: 0; padding: 0; }
  html, body { width: 1200px; height: 1200px; overflow: hidden; }
  body { background: var(--backdrop); position: relative; font-family: "Open Sans", Arial, sans-serif; }

  .rack-card { position: absolute; top: 80px; width: 440px; height: 990px; background: var(--paper); overflow: hidden; }
  .rack-card--front { left: 118px; }
  .rack-card--back { left: 643px; }

  .band { position: absolute; left: 0; width: 100%; background: linear-gradient(90deg, var(--orange-deep), var(--orange) 50%, var(--orange-deep)); }

  .brand { position: absolute; left: 0; width: 100%; display: flex; align-items: center; justify-content: center; gap: 12px; }
  .brand__mark { background: var(--orange); flex: none; }
  .brand__name { font-family: "Oswald", sans-serif; font-weight: 500; color: var(--charcoal); text-transform: uppercase; letter-spacing: 1px; line-height: 1.05; }

  .brand--front { top: 50px; }
  .brand--front .brand__mark { width: 56px; height: 56px; }
  .brand--front .brand__name { font-size: 27px; }

  .brand--back { top: 772px; gap: 8px; }
  .brand--back .brand__mark { width: 30px; height: 30px; }
  .brand--back .brand__name { font-size: 16px; }

  .headline { top: 181px; height: 121px; text-align: center; font-family: "Oswald", sans-serif; text-transform: uppercase; line-height: 1.1; padding-top: 20px; }
  .headline__strong { display: block; color: var(--paper); font-weight: 600; font-size: 38px; letter-spacing: -0.5px; }
  .headline__light { display: block; color: var(--charcoal); font-weight: 300; font-size: 40px; }

  .photo { position: absolute; border: 1px solid #6d6d6d; }
  .photo--bedroom { left: 24px; top: 312px; width: 146px; height: 142px; background: linear-gradient(180deg, #eeeae3, #cdbfae); }
  .photo--living { left: 24px; top: 477px; width: 146px; height: 142px; background: linear-gradient(180deg, #e6d8c2, #c77a3a); }
  .photo--kitchen { left: 24px; top: 642px; width: 146px; height: 143px; background: linear-gradient(180deg, #d9d9d6, #3a3634); }
  .photo--lounge { left: 181px; top: 312px; width: 234px; height: 473px; background: linear-gradient(180deg, #a8978a, #efe6dc 45%, #c79e74); }

  .welcome { top: 794px; height: 140px; text-align: center; padding: 16px 30px 0; }
  .welcome__title { font-family: "Oswald", sans-serif; font-weight: 600; color: var(--paper); font-size: 52px; line-height: 1; text-transform: uppercase; letter-spacing: -0.5px; }
  .welcome__text { margin-top: 8px; font-size: 12.6px; line-height: 1.33; color: var(--ink); text-align: justify; text-align-last: center; }

  .site-footer { position: absolute; left: 0; top: 940px; width: 100%; height: 50px; background: linear-gradient(90deg, var(--footer-dark), var(--footer-light) 50%, var(--footer-dark)); color: var(--paper); font-size: 15px; letter-spacing: 0.4px; text-align: center; line-height: 50px; }

  .service-tile { position: absolute; left: 24px; width: 113px; height: 117px; color: var(--paper); text-align: center; font-size: 12.5px; text-transform: uppercase; }
  .service-tile--orange { background: var(--orange); }
  .service-tile--grey { background: var(--charcoal); }
  .service-tile svg { position: absolute; left: 50%; top: 16px; transform: translateX(-50%); }
  .service-tile__label { position: absolute; left: 0; bottom: 16px; width: 100%; }
  .service-tile--kitchens { top: 24px; }
  .service-tile--bathrooms { top: 173px; }
  .service-tile--additions { top: 320px; }
  .service-tile--homes { top: 467px; }

  .photo--dining { left: 147px; top: 24px; width: 267px; height: 558px; background: linear-gradient(180deg, #a8896a, #cfd9e0 45%, #6e5640 75%, #3c2a1c); }

  .services { top: 600px; height: 148px; text-align: center; padding: 20px 30px 0; }
  .services__title { font-family: "Oswald", sans-serif; font-weight: 500; color: var(--paper); font-size: 16.5px; text-transform: uppercase; }
  .services__subtitle { font-family: "Oswald", sans-serif; font-weight: 400; color: var(--ink); font-size: 16.5px; text-transform: uppercase; margin-top: 5px; }
  .services__text { margin-top: 7px; font-size: 12.3px; line-height: 1.36; color: var(--paper); text-align: justify; text-align-last: center; }

  .contact { position: absolute; left: 0; top: 862px; width: 100%; text-align: center; font-size: 14px; color: var(--ink); line-height: 21px; }
  .contact li { list-style: none; display: flex; align-items: center; justify-content: center; gap: 6px; }
  .contact svg { flex: none; }
</style>
</head>
<body>

<section class="rack-card rack-card--front">
  <div class="brand brand--front">
    <span class="brand__mark"></span>
    <span class="brand__name">"T" Ridgeline<br>Builders</span>
  </div>

  <header class="band headline">
    <span class="headline__strong">Let us fix what your home</span>
    <span class="headline__light">inspector finds!</span>
  </header>

  <div class="photo photo--bedroom" role="img" aria-label="Bright remodeled bedroom with bed and windows"></div>
  <div class="photo photo--living" role="img" aria-label="Living room with fireplace, sofas and wood floor"></div>
  <div class="photo photo--kitchen" role="img" aria-label="Modern kitchen with dark cabinets and island"></div>
  <div class="photo photo--lounge" role="img" aria-label="Open lounge with cream sectional sofa and spiral staircase"></div>

  <div class="band welcome">
    <h1 class="welcome__title">Welcome!</h1>
    <p class="welcome__text">Whether it's getting your home remodeled or fixing damage that's been done to your home, we're here to help you every step of the way.</p>
  </div>

  <footer class="site-footer">www.brambleworkhomes.example</footer>
</section>

<section class="rack-card rack-card--back">
  <div class="service-tile service-tile--orange service-tile--kitchens">
    <svg width="60" height="60" viewBox="0 0 60 60" fill="none" stroke="#fff" stroke-width="3" stroke-linecap="round" stroke-linejoin="round">
      <path d="M22 4c-3 3 3 5 0 8M30 4c-3 3 3 5 0 8M38 4c-3 3 3 5 0 8"/>
      <path d="M16 20h28c0 8-6 13-14 13s-14-5-14-13z" fill="#fff"/>
      <path d="M8 26l4 16 10 10M52 26l-4 16-10 10"/>
    </svg>
    <span class="service-tile__label">Kitchens</span>
  </div>

  <div class="service-tile service-tile--grey service-tile--bathrooms">
    <svg width="64" height="60" viewBox="0 0 64 60" fill="none" stroke="#fff" stroke-width="3" stroke-linecap="round">
      <path d="M36 24c6-10 14-14 20-10" />
      <path d="M22 22l18 18" />
      <path d="M24 20c8-6 18 4 12 12z" fill="#fff"/>
      <path d="M16 32l-3 3M22 38l-3 3M28 44l-3 3M12 40l-3 3M18 46l-3 3M24 52l-3 3" stroke-width="2.5"/>
    </svg>
    <span class="service-tile__label">Bathrooms</span>
  </div>

  <div class="service-tile service-tile--orange service-tile--additions">
    <svg width="60" height="60" viewBox="0 0 60 60" stroke="#fff" stroke-width="4" stroke-linecap="round">
      <path d="M30 4v52M4 30h52"/>
    </svg>
    <span class="service-tile__label">Additions</span>
  </div>

  <div class="service-tile service-tile--grey service-tile--homes">
    <svg width="62" height="56" viewBox="0 0 62 56">
      <path d="M31 4L2 30h8v24h16V38h10v16h16V30h8z" fill="#fff"/>
    </svg>
    <span class="service-tile__label">Whole Homes</span>
  </div>

  <div class="photo photo--dining" role="img" aria-label="Dining nook with chandelier, bay windows and wooden table"></div>

  <div class="band services">
    <h2 class="services__title">Our Services</h2>
    <h3 class="services__subtitle">Residential or Commercial</h3>
    <p class="services__text">We've got all your needs covered: from residential remodels, to commercial damage repairs and everything in between. Don't hesitate to ask us a question or inquire as to why a certain process has to take place.</p>
  </div>

  <div class="brand brand--back">
    <span class="brand__mark"></span>
    <span class="brand__name">"T" Ridgeline<br>Builders</span>
  </div>

  <ul class="contact">
    <li>
      <svg width="10" height="13" viewBox="0 0 10 13"><path d="M5 0a5 5 0 0 1 5 5c0 3-5 8-5 8S0 8 0 5a5 5 0 0 1 5-5z" fill="#f29a1f"/><circle cx="5" cy="5" r="1.8" fill="#fff"/></svg>
      1207 Cinder Lane, Maplecrest, Florida 34999, United States
    </li>
    <li>
      <svg width="11" height="13" viewBox="0 0 11 13"><path d="M3 0l2 3-1.5 1.5c.5 2 2 3.5 3.5 4.5L8.5 7.5l2.5 2-1.5 3C5 12 1 7 0 1.5z" fill="#f29a1f"/></svg>
      555-318-4726
    </li>
    <li>
      <svg width="12" height="9" viewBox="0 0 12 9"><rect width="12" height="9" fill="#f29a1f"/><path d="M0 0l6 5 6-5" stroke="#fff" stroke-width="1.2" fill="none"/></svg>
      office@brambleworkhomes.example
    </li>
  </ul>

  <footer class="site-footer">www.brambleworkhomes.example</footer>
</section>

</body>
</html>
```